Fitness Centre/Personal Trainer Business Card

We need a business card design for a company based in Singapore called 'Vigor Summit'.

We are a team of Personal Trainers and we are planning to open our new training facility.

This design will also be printed/painted on the walls in our gym.

We are a new breed of personal trainers who take fitness seriously and holistically. We do not merely train our clients to be big and muscular.

We believe in wholeness. In our opinion, fitness should include: strength, speed, flexibility, mobility, stamina & agility. These are what we train for. Of course, nutrition/diet is key.

We use fitness tools such as kettlebells, QLV, Pylometric boxes, battling ropes, clubbells, medicine balls, bulgarian bags etc - functional and non-bulky tools.

I currently have a Facebook page 'Vigor Summit SG' which shows a logo of a kettlebell. But my business focus has since changed.

Services provided:
- Kettlebell Sport Preparation
- Calisthenics Training
- Corrective Exercises
- Sports Strength & Conditioning
- 28 days Weight Loss Program
- Myofascial Rehab Therapy
- Sports/Thai Massage

Main colors for the design should be BLACK & YELLOW. We envision a design which is able to protray the holistic view we take on fitness. Also it should somewhat appeal to the ladies and not intimidate them.

Target Market(s)

People between 18-35 years old. Students and working class alike.

Industry/Entity Type

Training

Requirements
Must have
• Name: Marcus Oleander Pryce
Fitness Coach
Corrective Exercise Specialist
M: +65 9372 6058
E: marcus@sgvigorsummit-example.com

Double-sided please.
Nice to have
• "What is your vigor summit?"

```html
<!DOCTYPE html>
<html lang="en">
<head>
<meta charset="utf-8">
<title>Vigor Summit – Business Card</title>
<link rel="stylesheet" href="https://fonts.googleapis.com/css2?family=Arimo:wght@400;700&family=Audiowide&display=swap">
<style>
  :root {
    --ink: #000000;
    --sun: #fbee00;
    --paper: #ffffff;
  }
  * { margin: 0; padding: 0; box-sizing: border-box; }
  html, body {
    width: 900px; height: 1200px; overflow: hidden;
    background: var(--paper);
    font-family: "Arimo", Arial, sans-serif;
  }
  .canvas { position: relative; width: 900px; height: 1200px; }

  /* Front side */
  .card-front {
    position: absolute; left: 12px; top: 80px; width: 876px; height: 515px;
    background: var(--sun); overflow: hidden;
  }
  .front-band {
    position: absolute; left: 0; top: 0; width: 100%; height: 358px;
    background: var(--ink);
  }
  .brand {
    position: absolute; right: 48px; top: 240px;
    display: flex; align-items: center; gap: 16px;
  }
  .brand-dot {
    width: 34px; height: 34px; border-radius: 50%;
    background: var(--sun);
  }
  .brand-name {
    font-family: "Audiowide", sans-serif;
    font-size: 52px; line-height: 1; color: var(--sun);
    text-transform: uppercase; letter-spacing: 1px;
  }
  .contact {
    position: absolute; left: 26px; top: 393px; color: var(--ink);
  }
  .contact-name { font-weight: 700; font-size: 21px; line-height: 26px; }
  .contact-line { font-size: 18px; line-height: 24px; }

  /* Back side */
  .card-back {
    position: absolute; left: 12px; top: 605px; width: 876px; height: 515px;
    background: var(--sun); overflow: hidden;
  }
  .bell-area {
    position: absolute; left: 273px; top: 20px; width: 330px; height: 430px;
    background: var(--paper);
    border-radius: 46% 46% 50% 50% / 38% 38% 62% 62%;
  }
  .services {
    position: absolute; left: 273px; top: 219px; width: 330px;
    text-align: center; color: var(--ink);
    font-size: 17px; line-height: 23.5px;
  }
  .services-title { font-weight: 700; font-size: 18px; }
  .services-list { list-style: none; }
  .tagline {
    position: absolute; left: 0; width: 100%; top: 463px;
    text-align: center; color: var(--ink);
    font-family: "Audiowide", sans-serif; font-size: 25px; letter-spacing: 0.5px;
  }
</style>
</head>
<body>
<main class="canvas">
  <section class="card-front">
    <div class="front-band"></div>
    <div class="brand">
      <span class="brand-dot"></span>
      <span class="brand-name">Vigor Summit</span>
    </div>
    <div class="contact">
      <p class="contact-name">Marcus Oleander Pryce</p>
      <p class="contact-line">Fitness Coach &amp; Corrective Exercise Specialist</p>
      <p class="contact-line">Mob: +65 9372 6058</p>
      <p class="contact-line">Email: marcus@sgvigorsummit-example.com</p>
    </div>
  </section>

  <section class="card-back">
    <div class="bell-area" role="img" aria-label="White kettlebell silhouette"></div>
    <div class="services">
      <p class="services-title">Services provided:</p>
      <ul class="services-list">
        <li>Kettlebell Sport Preparation,</li>
        <li>Calisthenics Training,</li>
        <li>Corrective Exercises,</li>
        <li>Sports Strength &amp; Conditioning,</li>
        <li>28 days Weight Loss Program,</li>
        <li>Myofascial Rehab Therapy,</li>
        <li>Sports/Thai Massage.</li>
      </ul>
    </div>
    <p class="tagline">"What is your vigor summit?"</p>
  </section>
</main>
</body>
</html>
```